SnackNook!!! A Vending Machine Business Looking for an attractive website.

We are a vending machine business in Northern Michigan. We have changed our name and have rebranded our company. We would like an attractive website that shares who we are, what services we provide, the products we offer in our machines, along with a form businesses can fill out to see if they are a good fit for our company. I would like to have a Home Page, About SnackNook, Why Choose SnackNook?, Products & Services, Contact Us (With a Login Option), and a page with a questionnaire for thos interested in getting a FREE Vending Machine.

Target Market(s)

Businesses, Campgrounds, Schools, and many more in Northern Michigan

Industry/Entity Type

Vending Machines

Coding

Coded - Design and coding required

Number of Pages Required

5+ page

Requirements
Must have
• An inviting and enticing Home Page. I want to get my potential clients engaged in our website.
Nice to have
• Possibly background photos from Northern Michigan
Should not have
• A corporate feel. I do not want a boring website.

```html
<!DOCTYPE html>
<html lang="en">
<head>
<meta charset="UTF-8">
<title>SnackNook — Crave. Vend. Repeat</title>
<link href="https://fonts.googleapis.com/css2?family=Alfa+Slab+One&family=Barlow:wght@400;500;600;700&display=swap" rel="stylesheet">
<style>
:root{
  --navy:#1b1e5c;
  --navy-deep:#141649;
  --navy-mid:#2a2f7a;
  --green:#2f5b26;
  --green-dark:#234a1d;
  --green-light:#3f7a33;
  --white:#ffffff;
  --ink:#1d1f4f;
  --muted:#555a7a;
  --steel:#b9bcc4;
}
*{box-sizing:border-box;margin:0;padding:0}
html,body{width:1200px;height:4252px;overflow:hidden;background:var(--navy)}
body{font-family:"Barlow",Arial,sans-serif;color:var(--white)}
.page{position:relative;width:1200px;height:4252px;overflow:hidden;background:var(--navy)}
.abs{position:absolute}
.display{font-family:"Alfa Slab One",Georgia,serif;font-weight:400;letter-spacing:.5px;white-space:nowrap}
.eyebrow{font-size:17px;letter-spacing:2.5px;font-weight:500}
.btn{position:absolute;display:flex;align-items:center;justify-content:center;border-radius:30px;font-size:13px;font-weight:700;letter-spacing:1px;text-transform:uppercase;color:var(--white);white-space:nowrap}
.btn-green{background:var(--green)}
.btn-blue{background:var(--navy-mid)}
.btn-outline{border:2px solid var(--white)}
.photo{position:absolute}

/* header */
.logo{font-family:"Alfa Slab One",Georgia,serif;color:var(--white);font-size:38px;display:flex;align-items:center;gap:10px;white-space:nowrap}
.logo-mark{width:12px;height:12px;background:var(--white)}
.nav{position:absolute;top:38px;left:530px;display:flex}
.nav a{font-family:"Alfa Slab One",Georgia,serif;font-size:10px;line-height:11px;color:var(--white);text-decoration:none;text-transform:uppercase;padding-left:14px;border-left:1px solid rgba(255,255,255,.5);white-space:nowrap}
.nav a:nth-child(1){border-left:none;padding-left:0;width:120px}
.nav a:nth-child(2){width:136px}
.nav a:nth-child(3){width:130px}
.nav a:nth-child(4){width:100px}
.login{position:absolute;left:1023px;top:33px;width:104px;height:33px;background:var(--green);font-family:"Alfa Slab One",serif;font-size:13px;display:flex;align-items:center;justify-content:center;border-radius:2px}

/* hero */
.hero-title{left:96px;top:240px;font-size:45px}
.hero-sub{left:96px;top:302px;font-size:31px}
.hero-tag{left:102px;top:357px;font-size:24px;font-weight:600;line-height:26px;text-transform:uppercase}

/* about */
.about-box{left:153px;top:759px;width:913px;height:317px;border:2px solid rgba(255,255,255,.75);border-radius:6px}
.section-title{font-size:38px;text-align:center;text-transform:uppercase}
.about-text{left:195px;top:824px;width:820px;font-size:19.5px;line-height:31px;text-align:center}

/* why */
.why-text p{font-size:18px;line-height:26px;margin-bottom:8px}

/* products */
.card{position:absolute;top:2046px;width:268px;height:413px;background:var(--white);border-radius:10px;color:var(--ink);overflow:hidden}
.card .machine{position:absolute;left:64px;top:30px;width:140px;height:208px;border-radius:4px}
.card h3{position:absolute;top:270px;width:100%;text-align:center;font-family:"Alfa Slab One",serif;font-weight:400;font-size:18px;color:var(--ink);white-space:nowrap}
.card p{position:absolute;top:298px;left:24px;right:24px;text-align:center;font-size:11.5px;line-height:15px;color:var(--muted)}
.card .btn{top:342px;left:62px;width:144px;height:42px;font-size:11px}
.card.fade{background:linear-gradient(90deg,#c8cbe0,#eeeef6 40%,#d6d8ea)}
.dots{left:545px;top:2502px;display:flex;gap:10px}
.dots span{width:40px;height:3px;background:var(--navy-mid)}
.dots span:first-child{background:var(--green-light)}

/* who */
.who-text p{font-size:19px;line-height:26px;margin-bottom:8px}

/* contact */
.contact-box{left:137px;top:3394px;width:965px;height:561px;border-radius:70px 24px 24px 24px;overflow:hidden;background:linear-gradient(180deg,#2e5a27,#2a5424 60%,#30612a)}
.field{position:absolute;height:50px;background:var(--white);display:flex;align-items:center;padding-left:18px;gap:10px;font-size:14px;color:#333}
.field svg{flex:none}
.field.area{align-items:flex-start;padding-top:16px}

/* footer */
.foot-nav{top:4114px;left:142px;display:flex;align-items:center;gap:20px;font-family:"Alfa Slab One",serif;font-size:14px;text-transform:uppercase;white-space:nowrap}
.foot-nav i{width:5px;height:5px;background:var(--white);border-radius:50%;display:block}
.copy{left:145px;top:4201px;font-size:14px}
.social{left:913px;top:4198px;display:flex;gap:17px}
.social span{width:22px;height:22px;border-radius:50%;background:var(--white);display:block}
</style>
</head>
<body>
<div class="page">

  <!-- HERO -->
  <div class="photo" role="img" aria-label="Northern Michigan town street at dusk" style="left:0;top:0;width:1200px;height:660px;background:radial-gradient(ellipse at 75% 30%,#2b3178 0%,#1d2164 45%,#1b1e5c 80%)"></div>
  <svg class="abs" style="left:0;top:0" width="1200" height="660" viewBox="0 0 1200 660">
    <circle cx="870" cy="165" r="395" fill="none" stroke="var(--green)" stroke-width="14"/>
    <circle cx="870" cy="165" r="385" fill="#262c74"/>
  </svg>
  <div class="photo" role="img" aria-label="Two stocked snack and drink vending machines side by side" style="left:619px;top:181px;width:470px;height:462px;border-radius:6px;background:linear-gradient(90deg,#2a2a2e 0%,#3a3b40 40%,#c7c9cf 55%,#e2e3e7 75%,#b9bcc4 100%)"></div>

  <div class="abs logo" style="left:124px;top:36px"><span class="logo-mark"></span>SnackNook</div>
  <nav class="nav">
    <a>About<br>SnackNook</a>
    <a>Why Choose<br>SnackNook?</a>
    <a>Products &amp;<br>Services</a>
    <a>Contact<br>SnackNook</a>
  </nav>
  <div class="login">LOGIN</div>

  <h1 class="abs display hero-title">SNACKNOOK</h1>
  <div class="abs display hero-sub">CRAVE. VEND. REPEAT</div>
  <div class="abs hero-tag">Elevating snacking,<br>one vend at a time</div>
  <div class="btn btn-green" style="left:104px;top:432px;width:170px;height:50px">Learn more</div>
  <div class="btn btn-blue" style="left:287px;top:432px;width:170px;height:50px">View products</div>

  <!-- ABOUT -->
  <div class="photo" role="img" aria-label="Faint aerial view of a Northern Michigan harbor town" style="left:0;top:660px;width:1200px;height:560px;background:linear-gradient(180deg,#1b1e5c 0%,#23286b 45%,#2a3072 70%,#1b1e5c 100%)"></div>
  <div class="abs about-box"></div>
  <div class="abs eyebrow" style="left:0;width:1212px;top:708px;text-align:center">OUR COMPANY</div>
  <h2 class="abs display section-title" style="left:0;width:1212px;top:734px"><span style="background:#1f2364;padding:0 18px">ABOUT SNACKNOOK</span></h2>
  <p class="abs about-text">At SnackNook, we don’t just vend snacks—we curate cravings. Our customized vending solutions bring flavor, convenience, and community to Northern Michigan. Whether you’re reaching for a mid-morning snack, a refreshing beverage, or a satisfying breakfast burrito, SnackNook delivers delight with every bite</p>
  <div class="btn btn-outline" style="left:521px;top:980px;width:169px;height:48px">Learn more</div>

  <!-- WHY -->
  <svg class="abs" style="left:0;top:1150px" width="1200" height="740" viewBox="0 0 1200 740">
    <path d="M0 100 Q600 -70 1200 80 L1200 620 Q600 770 0 620 Z" fill="#5a5ea8"/>
    <path d="M0 115 Q600 -40 1200 100 L1200 600 Q600 740 0 612 Z" fill="var(--green)"/>
  </svg>
  <div class="photo" role="img" aria-label="Aerial view of a green Northern Michigan town by the water" style="left:0;top:1260px;width:1200px;height:470px;background:radial-gradient(ellipse at 40% 60%,rgba(70,120,60,.55),rgba(47,91,38,0) 70%)"></div>
  <svg class="abs" style="left:620px;top:1255px" width="560" height="500" viewBox="0 0 560 500">
    <circle cx="305" cy="245" r="244" fill="#ffffff"/>
    <circle cx="305" cy="245" r="236" fill="#283078"/>
  </svg>
  <div class="photo" role="img" aria-label="Three stocked vending machines in a row" style="left:628px;top:1345px;width:495px;height:340px;border-radius:6px;background:linear-gradient(90deg,#c9cbd1,#2c2d31 25%,#3b3c42 55%,#d5d7dc 70%,#aeb1b9)"></div>
  <div class="abs eyebrow" style="left:136px;top:1311px;font-size:15px">WHY CHOOSE US</div>
  <h2 class="abs display" style="left:136px;top:1338px;font-size:38px">WHY SNACKNOOK ?</h2>
  <div class="abs why-text" style="left:144px;top:1410px;width:450px">
    <p>At SnackNook, we’re more than vending machines; we’re flavor architects, community connectors, and taste trailblazers. Imagine a world where every snack is an adventure, every sip a celebration. That’s the SnackNook promise—a symphony of taste, convenience, and camaraderie.</p>
    <p>Our Tailored Temptations await: from salty to sweet, our snack selection dances with variety.</p>
  </div>
  <div class="btn btn-outline" style="left:148px;top:1653px;width:192px;height:50px;font-size:15px">Learn more</div>

  <!-- PRODUCTS -->
  <div class="abs eyebrow" style="left:0;width:1212px;top:1930px;text-align:center;font-size:16px">WHAT WE OFFER</div>
  <h2 class="abs display section-title" style="left:0;width:1200px;top:1953px">OUR PRODUCTS</h2>

  <div class="card" style="left:104px">
    <div class="machine" role="img" aria-label="Glass-front drink vending machine" style="background:linear-gradient(90deg,#2f4fa8,#7fa4e0 60%,#c5c8cf 80%,#9da1aa)"></div>
    <h3>VENDOR MACHINE</h3>
    <p>Lorem ipsum dolor sit amet, consectetur adipiscing elit sed d</p>
    <div class="btn btn-green">Learn more</div>
  </div>
  <div class="card" style="left:393px">
    <div class="machine" role="img" aria-label="Snack vending machine with blue trim" style="background:linear-gradient(90deg,#3a3b40,#8b7d6a 40%,#b7bcc6 75%,#4c78d0)"></div>
    <h3>VENDOR MACHINE</h3>
    <p>Lorem ipsum dolor sit amet, consectetur adipiscing elit sed d</p>
    <div class="btn btn-green">Learn more</div>
  </div>
  <div class="card" style="left:681px">
    <div class="machine" role="img" aria-label="Snack vending machine with black keypad panel" style="background:linear-gradient(90deg,#c4c7cd,#3e4a8a 30%,#5b6090 60%,#222 80%,#c4c7cd)"></div>
    <h3>VENDOR MACHINE</h3>
    <p>Lorem ipsum dolor sit amet, consectetur adipiscing elit sed d</p>
    <div class="btn btn-green">Learn more</div>
  </div>
  <div class="card fade" style="left:972px">
    <div class="machine" role="img" aria-label="Combination snack and drink vending machine" style="background:linear-gradient(90deg,#8f93a6,#a48e7b 45%,#c3c6d0)"></div>
    <h3>VENDOR MACHINE</h3>
    <p>Lorem ipsum dolor sit amet, consectetur adipiscing elit sed d</p>
    <div class="btn btn-green">Learn more</div>
  </div>
  <div class="abs dots"><span></span><span></span><span></span></div>

  <!-- WHO -->
  <svg class="abs" style="left:0;top:2570px" width="560" height="760" viewBox="0 0 560 760">
    <path d="M0 20 Q420 -30 520 330 Q530 380 520 420 L0 700 Z" fill="var(--green)"/>
  </svg>
  <div class="photo" role="img" aria-label="Hand pressing the keypad of a vending machine" style="left:0;top:2612px;width:512px;height:650px;border-radius:0 420px 300px 0;background:linear-gradient(120deg,#3c3f47 0%,#6d7280 35%,#a9b2c4 60%,#3a5fa8 100%)"></div>
  <div class="photo" role="img" aria-label="Glass-front drink vending machine" style="left:256px;top:2929px;width:247px;height:379px;background:linear-gradient(90deg,#dfe2e8 0%,#3f66c2 8%,#6c92d8 55%,#2f55b0 80%,#b9bcc4 85%,#8d9099)"></div>
  <div class="abs eyebrow" style="left:607px;top:2688px;font-size:18px">SNACKNOOK</div>
  <h2 class="abs display" style="left:607px;top:2715px;font-size:38px">WHO WE ARE</h2>
  <div class="abs who-text" style="left:614px;top:2793px;width:520px">
    <p>We’re not just about vending machines; we’re your culinary companions, your flavor curators,</p>
    <p>and your secret stash of happiness.We’re the ones who believe that a vending machine isn’t just a metal box; it’s a portal to delight.</p>
    <p>Our mission? To transform mundane moments into memorable bites. Marcus and Elena, the dynamic duo behind SnackNook, have a passion for all things tasty. With backgrounds in sales and a penchant for personal connections, they’ve transformed the vending experience into an art form.</p>
  </div>
  <div class="btn btn-outline" style="left:612px;top:3123px;width:168px;height:48px">Learn more</div>

  <!-- CONTACT -->
  <svg class="abs" style="left:0;top:3700px" width="1200" height="280" viewBox="0 0 1200 280">
    <path d="M0 210 Q90 150 180 140 L180 165 Q90 175 0 230 Z" fill="var(--green-light)"/>
    <path d="M1060 105 Q1140 105 1200 140 L1200 160 Q1140 125 1060 120 Z" fill="var(--green-light)"/>
  </svg>
  <div class="abs contact-box" role="img" aria-label="Faded aerial view of a Northern Michigan town"></div>
  <div class="abs eyebrow" style="left:0;width:1212px;top:3442px;text-align:center;font-size:17px">GET IN TOUCH</div>
  <h2 class="abs display" style="left:0;width:1212px;top:3467px;text-align:center;font-size:35px">CONTACT US</h2>
  <div class="abs" style="left:568px;top:3520px;width:80px;height:3px;background:var(--white)"></div>

  <div class="field" style="left:231px;top:3564px;width:371px">
    <svg width="14" height="14" viewBox="0 0 14 14"><circle cx="7" cy="4" r="3.3" fill="#9a9a9a"/><path d="M1 14 Q7 5 13 14 Z" fill="#9a9a9a"/></svg>First Name</div>
  <div class="field" style="left:617px;top:3564px;width:373px">
    <svg width="14" height="14" viewBox="0 0 14 14"><circle cx="7" cy="4" r="3.3" fill="#9a9a9a"/><path d="M1 14 Q7 5 13 14 Z" fill="#9a9a9a"/></svg>Last Name</div>
  <div class="field" style="left:231px;top:3626px;width:371px">
    <svg width="15" height="12" viewBox="0 0 15 12"><rect x="0" y="0" width="15" height="12" rx="1.5" fill="#9a9a9a"/><path d="M1 1 L7.5 6.5 L14 1" stroke="#fff" stroke-width="1.3" fill="none"/></svg>Email address</div>
  <div class="field" style="left:617px;top:3626px;width:373px">
    <svg width="14" height="14" viewBox="0 0 14 14"><path d="M3 0.5 L5.5 3.5 L4 5.5 Q5.5 8.5 8.5 10 L10.5 8.5 L13.5 11 L11.5 13.5 Q4 13 0.5 3 Z" fill="#9a9a9a"/></svg>Phone</div>
  <div class="field area" style="left:231px;top:3693px;width:759px;height:127px">
    <svg width="15" height="13" viewBox="0 0 15 13"><ellipse cx="7.5" cy="5.5" rx="7" ry="5" fill="#c6c6c6"/><path d="M3 9 L2 13 L6 10 Z" fill="#c6c6c6"/></svg>Message</div>
  <div class="btn btn-outline" style="left:512px;top:3843px;width:209px;height:48px;font-size:15px">Send message</div>

  <!-- FOOTER -->
  <div class="abs logo" style="left:0;width:1236px;top:3998px;justify-content:center;font-size:40px"><span class="logo-mark"></span>SnackNook</div>
  <div class="abs foot-nav">
    <span>Home</span><i></i><span>About SnackNook</span><i></i><span>Why Choose SnackNook?</span><i></i><span>Products &amp; Services</span><i></i><span>Contact Us</span>
  </div>
  <div class="abs copy">Copyright © 2024 SnackNook. All rights reserved.</div>
  <div class="abs social" aria-label="Social links"><span></span><span></span><span></span><span></span></div>

</div>
</body>
</html>
```